Dog care service needs business card design

Our company is Paws Harbour. We provide care for dogs while their owners are away, either through home visits or a holiday stay in the homes of carefully selected minders. Our existing website & Chatterbook cover should provide all the colour cues for our business cards - namely blues, blondes and grey. We have an existing logo (provided).

www.pawsharbourcare.example.au
www.facebook.com/pawsharbourcareau

We wish to clearly communicate our three areas of service "dog minding, home visits, dog walking".

We would like to have the files ready for upload to Printlyne (or similar) for immediate printing.

Target Market(s)

Dog owners who love their dogs like family

Industry/Entity Type

Business

Contact Information for Business Card

Paws Harbour
Ph: 0417 358 904

Font styles to use
Sans Serif

Colors
33a6d7
3176b5

Requirements
Must have
• Logo
• Telephone number
• website
• "Dog minding, home visits, dog walking"
Should not have
• any additional illustrations beyond the logo.

```html
<!DOCTYPE html>
<html lang="en">
<head>
<meta charset="utf-8">
<title>Paws Harbour – Business Card</title>
<link href="https://fonts.googleapis.com/css2?family=Outfit:wght@500&family=Mulish:wght@700;800&display=swap" rel="stylesheet">
<style>
  :root {
    --ink: #3a4250;
    --blue: #33a6d7;
    --blue-deep: #3176b5;
    --card: #ffffff;
    --backdrop: #e9e9ec;
  }
  * { margin: 0; padding: 0; box-sizing: border-box; }
  html, body { width: 1200px; height: 600px; overflow: hidden; }
  body {
    background: var(--backdrop);
    font-family: "Mulish", sans-serif;
    position: relative;
  }
  .card {
    position: absolute;
    top: 152px;
    width: 467px;
    height: 278px;
    background: var(--card);
    border-radius: 16px;
    box-shadow: 0 4px 14px rgba(0,0,0,0.08);
    overflow: hidden;
  }
  .card--front { left: 93px; }
  .card--back { left: 639px; }

  /* Brand lockup: square + stacked name + tagline */
  .brand {
    display: flex;
    align-items: flex-start;
  }
  .brand__mark {
    flex: none;
    background: var(--blue);
  }
  .brand__text { display: flex; flex-direction: column; align-items: center; }
  .brand__name {
    font-family: "Outfit", sans-serif;
    font-weight: 500;
    color: var(--ink);
    line-height: 0.88;
    text-align: left;
    align-self: stretch;
  }
  .brand__tagline {
    font-family: "Mulish", sans-serif;
    font-weight: 800;
    color: var(--blue);
    text-transform: uppercase;
    white-space: nowrap;
  }

  .card--front .brand {
    position: absolute;
    left: 0; right: 0; top: 100px;
    justify-content: center;
    gap: 18px;
  }
  .card--front .brand__mark { width: 22px; height: 22px; margin-top: 10px; }
  .card--front .brand__name { font-size: 41px; }
  .card--front .brand__tagline {
    font-size: 12.5px;
    letter-spacing: 4.6px;
    margin-top: 10px;
    margin-right: -4.6px;
  }

  .back-content { text-align: center; }
  .card--back .brand {
    justify-content: center;
    gap: 10px;
    padding-top: 30px;
  }
  .card--back .brand__mark { width: 12px; height: 12px; margin-top: 6px; }
  .card--back .brand__name { font-size: 27px; }
  .card--back .brand__tagline {
    font-size: 9px;
    letter-spacing: 3.2px;
    margin-top: 6px;
    margin-right: -3.2px;
  }
  .contact {
    margin-top: 36px;
    color: var(--ink);
    font-weight: 800;
    font-size: 14px;
    line-height: 1.15;
  }
  .services {
    margin-top: 26px;
    color: var(--blue);
    font-weight: 800;
    font-size: 12.5px;
    letter-spacing: 0.1px;
  }
</style>
</head>
<body>
  <section class="card card--front" aria-label="Business card front">
    <div class="brand">
      <span class="brand__mark" aria-hidden="true"></span>
      <div class="brand__text">
        <span class="brand__name">Paws<br>Harbour</span>
        <span class="brand__tagline">Pet Services</span>
      </div>
    </div>
  </section>

  <section class="card card--back" aria-label="Business card back">
    <div class="back-content">
      <div class="brand">
        <span class="brand__mark" aria-hidden="true"></span>
        <div class="brand__text">
          <span class="brand__name">Paws<br>Harbour</span>
          <span class="brand__tagline">Pet Services</span>
        </div>
      </div>
      <p class="contact">
        Phone: 0417 358 904<br>
        www.pawsharbourcare.example.au
      </p>
      <p class="services">DOG MINDING - HOME VISITING - DOG WALKING</p>
    </div>
  </section>
</body>
</html>
```